Gum Care Season infographic - Bright Grins for Every Year

To create an infographic for Gum Care Season, August 2014, with the key messages of how the health of your mouth affects you through your lifetime.
We require two posters (A3 and A4 options) that will educate the Australian and New Zealand public of the importance of maintaining good oral health through facts and statistics (see attachments), focusing on different stages in your life.
The A3 poster will be used for: hanging in dental practices, posted in social media, on websites, advertising, public relations.
The A4 poster will be used for print handouts, websites, advertising, public relations.
Sections of the posters will be pulled out to be used in social media posts, on websites, in emails, etc.
Design constraints:
Poster One: Infographic Poster to be A3 (Appendix 1)
Poster Two: Infographic Poster to be reconfigured as A4 handout with limited facts (Appendix 2).
Full colour with the PVR colour palette reflected throughout.
Deliverables:
Design two infographics to reflect the tagline, Bright Grins for Every Year, and:
• One A3 poster to represents the key milestones as outlined in Appendix 1.
One A4 poster/handout to represent the key milestones in Appendix 2.
• Is obvious that these are stages in your life but does not mention the specific ages.
• Facts can be represented in icons, images, graphs, fractions, percentages, etc.
• Can be broken into smaller campaign sub messages.
• Includes: Gum Care Season and Bright Grins for Every Year text.
• Includes: A PVR Initiative logo.
• Includes August 2014 as Gum Care Season.
• Include website: www.pivoradental.example
• Is similar in style to the PVR launch infographic (attached).
• Clean, vibrant, understandable and friendly.
Tone:
PVR is experienced, reliable, caring, accessible, knowledgeable, friendly and confident in all aspects of dentistry.
The infographic can be ‘Tongue in cheek’ – friendly tone to suit different age groups through the messages, ie. 18-25 years is more conversational and cheeky, while 50+ could come from a ‘dad joke.’
See attached logo, colour palette and appendices.
Target Market(s)
Aussie and Kiwi families visiting a modern, bright, well-presented dental practice.
Industry/Entity Type
Health
Requirements
Must have
- Bright, clear and engaging. Needs to be suited to a professional dental practice, but also stand out on social media and in advertising.
Must have name of campaign and month, brand supporter, website - see brief.

```html
<!DOCTYPE html>
<html lang="en">
<head>
<meta charset="utf-8">
<title>Gum Care Season – Bright Grins for Every Year</title>
<link href="https://fonts.googleapis.com/css2?family=Open+Sans:wght@300;400;700;800&family=Oswald:wght@400;600;700&display=swap" rel="stylesheet">
<style>
:root{
  --blue-light:#27a6e3;
  --blue-mid:#1a8fd2;
  --blue-deep:#0f62a8;
  --navy:#13467f;
  --yellow:#f6c219;
  --band:#e9f4fc;
  --white:#ffffff;
  --soft:#cfe8f8;
}
*{margin:0;padding:0;box-sizing:border-box}
html,body{width:851px;height:1200px;overflow:hidden}
body{font-family:"Open Sans",sans-serif;color:var(--white);background:var(--blue-deep)}
.poster{position:relative;width:851px;height:1200px;overflow:hidden;
  background:radial-gradient(ellipse at 50% 20%,var(--blue-light) 0%,var(--blue-mid) 40%,var(--blue-deep) 100%)}
.abs{position:absolute}
.mascot{left:40px;top:18px;width:120px;height:200px;border-radius:50px 50px 30px 30px;
  background:linear-gradient(180deg,#ffffff,#d9ecf8)}
.title-small{left:185px;top:32px;font-family:"Oswald",sans-serif;font-weight:600;font-size:31px;letter-spacing:.5px}
.title-big{left:185px;top:78px;width:380px;font-family:"Oswald",sans-serif;font-weight:700;font-size:44px;line-height:50px;text-transform:uppercase}
.brand{left:590px;top:40px;display:flex;align-items:center;gap:12px}
.brand-dot{width:18px;height:18px;border-radius:50%;background:var(--white)}
.brand-name{font-weight:800;font-size:62px;letter-spacing:2px}
.brand-sub{left:620px;top:118px;font-weight:800;font-size:20px;letter-spacing:.5px}
.timeline{left:40px;top:258px;width:2px;height:850px;border-left:2px dotted var(--soft)}
.age-tab{left:0;height:26px;padding:0 22px;background:var(--yellow);color:var(--navy);
  font-weight:800;font-size:15px;line-height:26px;clip-path:polygon(0 0,92% 0,100% 50%,92% 100%,0 100%)}
.band{left:60px;width:730px;height:28px;background:var(--band);color:var(--navy);
  font-family:"Oswald",sans-serif;font-weight:700;font-size:18px;line-height:28px;padding-left:90px;letter-spacing:.5px}
.big{font-weight:300;line-height:1}
.note{font-size:12px;line-height:15px;color:var(--white)}
.note b{font-weight:800}
.map{left:408px;top:318px;width:80px;height:66px;border-radius:40% 55% 45% 50%;background:linear-gradient(135deg,#ffffff,#bcdcf2);opacity:.85}
.footer{left:150px;top:1122px;width:550px;height:50px;background:var(--band);color:var(--navy);text-align:center;
  font-family:"Oswald",sans-serif}
.footer .f1{font-weight:700;font-size:24px;line-height:30px}
.footer .f2{font-weight:400;font-size:14px;line-height:18px}
.web{left:0;top:1180px;width:851px;text-align:center;font-size:13px;font-weight:700}
</style>
</head>
<body>
<div class="poster">

  <div class="abs mascot" role="img" aria-label="Friendly cartoon tooth mascot"></div>
  <div class="abs title-small">GUM CARE SEASON AND</div>
  <div class="abs title-big">Bright Grins for Every Year</div>

  <div class="abs brand"><span class="brand-dot"></span><span class="brand-name">PVR</span></div>
  <div class="abs brand-sub">Pivora Dental</div>

  <div class="abs timeline"></div>

  <!-- General facts -->
  <div class="abs age-tab" style="top:250px">AGE</div>
  <div class="abs band" style="top:280px">GENERAL DENTAL FACTS</div>
  <div class="abs big" style="left:110px;top:322px;font-size:66px">90%</div>
  <div class="abs note" style="left:250px;top:338px;width:170px">of all dental disease<br>is <b>preventable</b></div>
  <div class="abs map" role="img" aria-label="Map of Australia"></div>
  <div class="abs big" style="left:480px;top:322px;font-size:66px">30%</div>
  <div class="abs note" style="left:640px;top:330px;width:175px">of <b>Australians</b> admit they are only brushing once daily</div>

  <!-- 18-25 -->
  <div class="abs age-tab" style="top:418px">18–25 years</div>
  <div class="abs band" style="top:448px">WATCH YOUR MOUTH!</div>
  <div class="abs big" style="left:110px;top:488px;font-size:54px">50%</div>
  <div class="abs note" style="left:110px;top:546px;width:140px"><b>18–25 year olds</b> haven't visited a dentist within the past 12 months</div>
  <div class="abs big" style="left:290px;top:488px;font-size:54px">48%</div>
  <div class="abs note" style="left:290px;top:546px;width:140px">people remember a smile on <b>first impression</b> more than anything else</div>
  <div class="abs big" style="left:470px;top:488px;font-size:54px">83%</div>
  <div class="abs note" style="left:470px;top:546px;width:150px">say that stained teeth and <b>bad breath</b> are the biggest turn offs on a <b>first date</b></div>
  <div class="abs note" style="left:650px;top:500px;width:160px">A quarter <b>(25.8%)</b> of adults over the age of <b>15 reported</b> they feel self conscious about their dental appearance</div>

  <!-- 25-40 -->
  <div class="abs age-tab" style="top:612px">25–40 years</div>
  <div class="abs band" style="top:642px">WORKING ON IT!</div>
  <div class="abs big" style="left:110px;top:686px;font-size:58px">1 MILLION</div>
  <div class="abs note" style="left:110px;top:748px;width:280px">lost days of work each year</div>
  <div class="abs note" style="left:440px;top:690px;width:340px">The <b>total direct costs</b> and lost productivity due to poor dental health in Australia is <b>$2 billion</b>. Approximately <b>11%</b> of adults avoided eating certain foods because of problems.</div>

  <!-- 40-55 -->
  <div class="abs age-tab" style="top:778px">40–55 years</div>
  <div class="abs band" style="top:808px">LIKE PULLING TEETH!</div>
  <div class="abs big" style="left:110px;top:850px;font-size:52px">600,000 <span style="font-size:22px">days</span></div>
  <div class="abs note" style="left:110px;top:906px;width:200px">lost from school</div>
  <div class="abs big" style="left:400px;top:844px;font-size:58px">50%</div>
  <div class="abs note" style="left:400px;top:904px;width:170px">of <b>Aussie kids</b> have suffered from this preventable disease (tooth decay)</div>
  <div class="abs big" style="left:640px;top:844px;font-size:58px">68%</div>
  <div class="abs note" style="left:640px;top:904px;width:160px">of <b>2–5 year olds</b> have never visited a dentist</div>

  <!-- 55+ -->
  <div class="abs age-tab" style="top:958px">55+ years</div>
  <div class="abs band" style="top:986px">A GATEWAY TO HEALTH!</div>
  <div class="abs note" style="left:100px;top:1024px;width:160px;text-align:center">More than<br><span style="font-size:24px;font-weight:300;line-height:28px">90 percent</span><br>of all systemic diseases – including heart disease – have <b>oral symptoms</b></div>
  <div class="abs note" style="left:285px;top:1026px;width:140px;text-align:center">Half of people<br><span style="font-size:20px;font-weight:700;line-height:24px">aged 45–64</span><br>attended the dentist because of a problem</div>
  <div class="abs big" style="left:460px;top:1026px;font-size:50px">53%</div>
  <div class="abs note" style="left:460px;top:1078px;width:150px">of <b>65yrs+</b> have periodontal disease</div>
  <div class="abs note" style="left:645px;top:1024px;width:170px;text-align:center">People with periodontal disease may be more likely to have coronary artery disease than people with healthy mouths.</div>

  <!-- Footer -->
  <div class="abs footer">
    <div class="f1">GUM CARE SEASON</div>
    <div class="f2">AUGUST 2014</div>
  </div>
  <div class="abs web">www.pivoradental.example</div>

</div>
</body>
</html>
```